Modern Minimalistic Supplement Label

Opportunity for recurring projects with a growing company. We have provided a detailed creative brief and all necessary files and guidelines. If you have any questions we will be closely monitoring the discussion board and email provided.

THE NAMES LISTED IN THE BRIEF ARE DIFFERENT FROM THE LABEL TEMPLATES. This is a private label brand. The label templates given are generic so please examine the entire brief before starting.

Use the PSD mockups attached and pair the labels with the correct bottles.

Do not use an entirely white background.

This could be excellent portfolio material.

Start by looking at the "CREATIVE_BRIEF" file. Logo files are contained in the "58213907" zip file.

UPDATE* Use the following business address for the "manufactured for" box on the labels.

Fernwick
4817 Larkmoor Ave. #2209
Ann Arbor MI 48196

Target Market(s)

All information provided in "CREATIVE_BRIEF" file.

Industry/Entity Type

Supplement

Requirements
Must have
• All information provided in "CREATIVE_BRIEF" file.
Nice to have
Should not have

```html
<!DOCTYPE html>
<html lang="en">
<head>
<meta charset="utf-8">
<title>Fernwick EAA+Energy Label</title>
<link href="https://fonts.googleapis.com/css2?family=Oswald:wght@500&family=Roboto+Condensed:wght@400;700&family=Montserrat:wght@600;700&family=Archivo+Black&display=swap" rel="stylesheet">
<style>
  :root{
    --bg:#ececec;
    --label:#1c1b1e;
    --panel:#242327;
    --pink:#e8186d;
    --white:#ffffff;
    --muted:#d9d9d9;
  }
  html,body{margin:0;width:1200px;height:1200px;overflow:hidden;background:var(--bg);}
  .label{position:absolute;left:30px;top:452px;width:1140px;height:295px;background:var(--label);color:var(--white);font-family:"Roboto Condensed",sans-serif;}
  .front-field{position:absolute;left:394px;top:12px;width:340px;height:210px;background:linear-gradient(135deg,#2a292d 0%,#1f1e22 60%,#1c1b1e 100%);}
  .info-box{position:absolute;left:16px;width:210px;border:1px solid var(--muted);padding:3px 3px;box-sizing:border-box;font-size:7.6px;line-height:11.6px;text-align:justify;}
  .info-box .tag{color:var(--pink);font-weight:700;}
  .directions{top:12px;height:64px;}
  .warning{top:84px;height:76px;}
  .disclaimer{top:170px;height:36px;font-weight:700;font-size:6.4px;line-height:10px;}
  .mfg-head{position:absolute;left:16px;top:213px;color:var(--pink);font-weight:700;font-size:8px;}
  .mfg-box{position:absolute;left:16px;top:229px;width:194px;height:28px;border:1px solid var(--muted);box-sizing:border-box;font-family:"Montserrat",sans-serif;font-size:6.6px;display:flex;align-items:center;justify-content:center;}
  .brand{position:absolute;left:394px;width:340px;top:52px;text-align:center;font-family:"Montserrat",sans-serif;font-weight:700;font-size:22px;letter-spacing:3px;}
  .product{position:absolute;left:232px;width:648px;top:114px;text-align:center;font-family:"Oswald",sans-serif;font-weight:500;font-size:44px;line-height:50px;}
  .subtitle{position:absolute;left:232px;width:648px;top:170px;text-align:center;font-family:"Montserrat",sans-serif;font-weight:600;font-size:15px;letter-spacing:4px;}
  .flavor-band{position:absolute;left:232px;top:199px;width:648px;height:23px;background:var(--pink);text-align:center;font-family:"Montserrat",sans-serif;font-weight:600;font-size:12.5px;letter-spacing:4px;line-height:23px;}
  .rule{position:absolute;left:232px;top:226px;width:648px;height:1.5px;background:var(--white);}
  .tagline{position:absolute;left:232px;width:648px;top:238px;text-align:center;font-size:10.5px;letter-spacing:1.2px;}
  .rule-short{position:absolute;left:424px;top:259px;width:264px;height:1px;background:var(--muted);}
  .net{position:absolute;left:232px;width:648px;top:265px;text-align:center;font-size:8.6px;letter-spacing:1.6px;}
  .facts{position:absolute;left:887px;top:12px;width:238px;height:273px;border:1px solid var(--muted);box-sizing:border-box;padding:2px 3px;font-size:8.2px;line-height:12px;}
  .facts h2{margin:0;font-family:"Archivo Black",sans-serif;font-weight:400;font-size:17px;letter-spacing:2.4px;line-height:20px;}
  .facts .meta{font-size:7.6px;line-height:11px;}
  .facts b{font-weight:700;}
  .thick{height:3px;background:var(--muted);margin:2px 0;}
  .thin{height:1px;background:var(--muted);margin:1px 0;}
  .row{display:flex;justify-content:space-between;}
  .row .amt{display:flex;gap:14px;}
  .indent{padding-left:6px;}
  .list{padding-left:6px;text-align:justify;text-align-last:justify;}
  .list.last{text-align-last:left;}
  .note{font-size:7.4px;line-height:11px;}
  .ingredients{font-size:7.2px;line-height:10.5px;}
</style>
</head>
<body>
<div class="label">
  <div class="front-field"></div>

  <div class="info-box directions"><span class="tag">DIRECTIONS:</span> Stir 1 scoop with 6-8 ounces of cold water and consume in the morning and/or between meals. Pre-Workout, take 1 or more servings 20-30 minutes before activity. Post-Training, take 1 or more servings immediately after finishing activity.</div>
  <div class="info-box warning"><span class="tag">WARNING:</span> Check with a qualified health care professional before taking this product if you are pregnant or nursing a baby, under 18 years of age, have any known or suspected medical conditions, and/or if you are taking any prescription or OTC medications. <b>KEEP OUT OF REACH OF CHILDREN.</b></div>
  <div class="info-box disclaimer">*These statements have not been evaluated by the Food and Drug Administration. This product is not intended to diagnose, treat, cure, or prevent any disease.</div>
  <div class="mfg-head">MANUFACTURED FOR:</div>
  <div class="mfg-box">Manufactured for Orrin</div>

  <div class="brand">FERNWICK</div>
  <div class="product">EAA+ENERGY</div>
  <div class="subtitle">AMINO BLEND</div>
  <div class="flavor-band">RASPBERRY ICED TEA</div>
  <div class="rule"></div>
  <div class="tagline">FOR INCREASED ENERGY AND PROTEIN SYNTHESIS</div>
  <div class="rule-short"></div>
  <div class="net">NET WT. 360 G ( 12.7 OZ ) I DIETARY SUPPLEMENT</div>

  <div class="facts">
    <h2>Supplement Facts</h2>
    <div class="meta"><b>Serving Size:</b> 9g (1 Scoop)<br><b>Servings Per Container:</b> 40</div>
    <div class="thick"></div>
    <div class="row"><b>Amount Per Serving</b><b>%Daily Value</b></div>
    <div class="thin"></div>
    <div>Calories 5</div>
    <div class="thin"></div>
    <div class="row"><b>Total Carbohydrates</b><span class="amt"><span>2 g</span><span>1%</span></span></div>
    <div class="row indent"><span>Dietary Fiber</span><span class="amt"><span>2 g</span><span>8%</span></span></div>
    <div class="thin"></div>
    <div class="row"><b>Amino Blend</b><span style="margin-right:42px">5000 mg</span></div>
    <div class="list">(Taurine, L-Glutamine, L-Arginine, L-Leucine</div>
    <div class="list">L-Valine, L-Isoleucine, L-Citrulline, L-Tyrosine</div>
    <div class="list last">L-Theanine, L-Histidine, L-Lysine HCl, L-Threonine)</div>
    <div class="thin"></div>
    <div class="row"><b>Energy Blend</b><span style="margin-right:42px">175 mg</span></div>
    <div class="indent">(Caffeine, Theobromine, Green Tea Extract)</div>
    <div class="thick"></div>
    <div class="note">** Percent Daily Values are based upon a 2,000 calorie diet.<br>† Daily Value not Established</div>
    <div class="thin"></div>
    <div class="ingredients"><b>Ingredients:</b> (Chicory Root Powder) Inulin, Malic Acid, Natural Artificial Flavors, Raspberry Powder, Silicon Dioxide, Sucralose, Citric Acid, Acesulfame Potassium.</div>
  </div>
</div>
</body>
</html>
```